Bref créative
Stationary - Morvane Advisory
Business Card, Letterhead & Pen Design
Professional
Helmut Draven
Director
Address line 1
Address line 2
Address line 3
Address line 4
Post Code
QRP@QRP.example
For the business card I like the idea of front/back designs, where either there is something which joins the front and back or there is a slightly modified logo on the back... You're call, I'm open to anything here, so if you come up with something just try it out, I'll give everyone feedback where possible!
Please don't just stick my logo on a pen and say "hey, here you go...", for the pen design I'm looking for colours etc and where they are placed on the pen too!
Anything you think would look good!
Image file to show the logo
Extra images (inc psds!) for the logo

```html
<!DOCTYPE html>
<html lang="en">
<head>
<meta charset="utf-8">
<title>Morvane Advisory – Business Card</title>
<link href="https://fonts.googleapis.com/css2?family=Arimo:wght@400;700&display=swap" rel="stylesheet">
<style>
  :root {
    --stage: #676b71;
    --paper: #ffffff;
    --brand: #1a8fc4;
    --brand-deep: #0b5f8f;
    --brand-light: #4cb7e2;
    --ink: #3a3d42;
    --muted: #6f747a;
  }
  * { margin: 0; padding: 0; box-sizing: border-box; }
  html, body { width: 1200px; height: 901px; overflow: hidden; }
  body {
    background: var(--stage);
    font-family: "Arimo", Arial, sans-serif;
    position: relative;
  }
  .card {
    position: absolute;
    border-radius: 14px;
    overflow: hidden;
  }
  .card-front {
    left: 404px; top: 178px; width: 402px; height: 263px;
    background: var(--paper);
  }
  .front-logo {
    position: absolute; left: 26px; top: 26px;
    display: flex; align-items: center; gap: 10px;
  }
  .logo-square {
    width: 40px; height: 40px; border-radius: 6px;
    background: var(--brand);
  }
  .logo-name {
    font-weight: 700; font-size: 30px; color: var(--brand);
    letter-spacing: 0.5px; line-height: 1;
  }
  .holder {
    position: absolute; left: 102px; top: 94px;
  }
  .holder-name { font-size: 15px; color: var(--brand); }
  .holder-role { font-size: 10px; color: var(--muted); margin-top: 2px; }
  .address {
    position: absolute; left: 102px; top: 140px;
    font-size: 10px; line-height: 14px; color: var(--ink);
  }
  .contact {
    position: absolute; left: 102px; top: 202px;
    font-size: 10px; line-height: 14px; color: var(--ink);
  }
  .contact span { color: var(--brand); margin-right: 6px; }
  .front-watermark {
    position: absolute; left: 300px; top: 116px;
    width: 78px; height: 78px; border-radius: 10px;
    background: var(--brand);
    opacity: 0.08;
  }
  .front-band {
    position: absolute; left: 0; right: 0; bottom: 0; height: 16px;
    background: linear-gradient(180deg, var(--brand-light), var(--brand-deep));
  }
  .card-back {
    top: 462px; width: 472px; height: 273px;
    display: flex; align-items: center; justify-content: center; gap: 14px;
  }
  .card-back-white { left: 163px; background: var(--paper); }
  .card-back-blue {
    left: 640px;
    background: radial-gradient(ellipse at 50% 45%, var(--brand-light) 0%, var(--brand) 45%, var(--brand-deep) 100%);
  }
  .back-square {
    width: 64px; height: 64px; border-radius: 8px;
    background: var(--brand);
  }
  .card-back-blue .back-square { background: var(--paper); }
  .back-name {
    font-weight: 700; font-size: 28px; color: var(--brand);
  }
  .card-back-blue .back-name { color: var(--paper); }
</style>
</head>
<body>
  <section class="card card-front">
    <div class="front-logo">
      <div class="logo-square"></div>
      <div class="logo-name">Morvane Advisory</div>
    </div>
    <div class="holder">
      <p class="holder-name">Helmut Draven</p>
      <p class="holder-role">Director</p>
    </div>
    <div class="address">
      <p>Address line 1, Address line 2</p>
      <p>Address line 3, Address line 4</p>
      <p>Post Code</p>
    </div>
    <div class="contact">
      <p><span>T:</span>01632 960 418</p>
      <p><span>E:</span>QRP@QRP.example</p>
    </div>
    <div class="front-watermark" aria-hidden="true"></div>
    <div class="front-band"></div>
  </section>

  <section class="card card-back card-back-white">
    <div class="back-square"></div>
    <div class="back-name">Morvane Advisory</div>
  </section>

  <section class="card card-back card-back-blue">
    <div class="back-square"></div>
    <div class="back-name">Morvane Advisory</div>
  </section>
</body>
</html>
```